Build PowerPoint for New Logo & Letterhead

I have started my own consulting firm and created a logo and letterhead (attached) am looking PowerPoint template. My name is Dorrit Okonkwo-Haverly and the company is called Birchpoint Consulting. We primarily use PowerPoint files to display analyses, maps and key talking points from interviews and/or recommendations. We use the documents more to facilitate discussion with our target audiences. Most of the time our PowerPoint document is printed as handouts for our clients and not projected.

Target Market(s)

Healthcare provider organizations (hospitals, health systems, physician groups)

Industry/Entity Type

Healthcare

Font styles to use
Sans Serif

Colors
abd036
1f9ad1
0355a3

Requirements
Must have
• I would like to cover page to play off of the letterhead in some fashion. I want the design to provide plenty of space for text, graphics, maps, pictures, etc.
• We will usually include our clients logo somewhere on the document. Historically it is prominent on the cover page and then in one of the corners on all of the pages thereafter.

```html
<!DOCTYPE html>
<html lang="en">
<head>
<meta charset="utf-8">
<title>Birchpoint Consulting – Presentation Template</title>
<link rel="stylesheet" href="https://fonts.googleapis.com/css2?family=Open+Sans:wght@300;400;600;700&family=Roboto+Condensed:wght@400;700&display=swap">
<style>
:root{
  --green:#abd036;
  --green-dark:#8fbd2a;
  --sky:#1f9ad1;
  --blue:#0355a3;
  --mid-blue:#2f73b8;
  --page:#e3e4e6;
  --white:#ffffff;
  --ink:#6d6e71;
  --soft:#9a9b9e;
  --grey:#8a8b8d;
  --grey-light:#a4a5a7;
  --grey-dark:#6c6d70;
}
*{margin:0;padding:0;box-sizing:border-box}
html,body{width:1200px;height:893px;overflow:hidden;background:var(--page)}
body{position:relative;font-family:"Open Sans",Arial,sans-serif;color:var(--ink)}
.slide{position:absolute;width:355px;height:200px;background:var(--white);overflow:hidden}
.c1{left:53px}.c2{left:417px}.c3{left:782px}
.r1{top:39px}.r2{top:245px}.r3{top:451px}.r4{top:658px}
.abs{position:absolute}
.photo{position:absolute}
.slide-title{position:absolute;left:17px;top:17px;font-size:8.2px;color:var(--blue);font-weight:400;letter-spacing:.1px}
.title-rule{position:absolute;left:17px;top:29px;width:323px;height:.6px;background:#c9cacc}
.tiny{font-size:3.9px;line-height:5.4px;color:var(--soft);text-align:justify}
.tiny.center{text-align:center}
.footer-brand{position:absolute;left:5px;bottom:7px;font-size:5px;font-weight:700;color:var(--blue);display:flex;gap:8px;align-items:center}
.footer-brand .mark{width:5px;height:5px;background:var(--sky)}
.footer-band{position:absolute;left:0;bottom:0;width:355px;height:8px}
.page-no{position:absolute;right:7px;bottom:2px;font-size:3.5px;color:var(--white)}
.brand-name{font-weight:700;color:var(--blue);letter-spacing:.5px}
/* cover */
.cover .brand{position:absolute;left:37px;top:34px;display:flex;align-items:center;gap:5px;font-size:8px}
.cover .brand .mark{width:10px;height:10px;background:var(--sky)}
.welcome{position:absolute;right:22px;top:92px;text-align:right;color:var(--white)}
.welcome h1{font-family:"Roboto Condensed",Arial Narrow,sans-serif;font-weight:400;font-size:17px;letter-spacing:.3px;line-height:17px}
.welcome p.sub{font-size:8.4px;letter-spacing:2.4px;font-weight:300;margin-top:1px}
.welcome p.date{font-size:5px;margin-top:6px}
.cover .legal{position:absolute;left:33px;top:173px;width:200px;font-size:3.2px;line-height:4.2px;color:var(--soft)}
.cover .partner{position:absolute;right:22px;top:172px;font-size:6.5px;font-weight:700;color:var(--blue)}
/* toc */
.toc-kicker{position:absolute;left:39px;top:38px;font-size:5.2px;color:var(--sky)}
.toc-title{position:absolute;left:39px;top:46px;font-size:13.5px;font-weight:300;color:var(--green-dark)}
.toc-list{position:absolute;top:96px;list-style:none}
.toc-list li{display:flex;align-items:center;gap:6px;height:20px;font-size:5.2px;color:var(--ink)}
.toc-list .dot{width:11px;height:11px;border-radius:50%;background:var(--green);color:var(--white);font-size:3.5px;display:flex;align-items:center;justify-content:center}
/* vision */
.vision .label{position:absolute;left:22px;top:16px;font-size:8px;color:var(--white);font-weight:300}
.vision .pillar{position:absolute;top:82px;width:120px;text-align:center}
.vision .badge{width:38px;height:38px;margin:0 auto;border-radius:50%;border:2.5px solid var(--white);background:var(--green);display:flex;align-items:center;justify-content:center}
.vision .pillar p{margin-top:8px;font-size:5.1px;line-height:7px;color:var(--white);font-weight:300}
/* team */
.member{position:absolute;top:52px;width:80px;text-align:center}
.member .portrait{width:40px;height:40px;margin:0 auto;border-radius:50%;border:2.5px solid var(--green)}
.member h3{margin-top:5px;font-size:4.6px;font-weight:400;color:var(--sky)}
.member h4{font-size:3.4px;font-weight:400;color:var(--ink);margin-bottom:5px}
/* donuts */
.donut{position:absolute;top:62px;width:90px;text-align:center}
.donut .tiny{margin-top:7px}
/* bar chart legend */
.legend{position:absolute;left:247px;top:121px;width:90px;font-size:3.4px;line-height:4.3px;color:var(--soft)}
.legend .key{color:var(--ink);display:flex;align-items:center;gap:4px}
.legend .key + p{padding-left:8px}
.legend .swatch{width:4px;height:4px}
/* services */
.service{position:absolute;top:50px;width:71px;height:112px;background:var(--grey-light)}
.service .head{height:46px;display:flex;flex-direction:column;align-items:center;justify-content:flex-end;padding-bottom:3px;color:var(--white);font-size:5.2px;line-height:6.4px;text-align:center}
.service .head.dark{background:var(--grey-dark)}
.service .head.lime{background:var(--green)}
.service .tiny{color:var(--white);padding:4px 5px;text-align:center;font-size:4.1px}
/* section */
.section-name{position:absolute;left:0;width:355px;top:134px;text-align:center;font-size:10.5px;font-weight:300;color:var(--sky)}
/* image text */
.image-text .panel{position:absolute;left:0;top:0;width:153px;height:200px;background:var(--mid-blue)}
.image-text h2{position:absolute;left:19px;top:17px;font-size:8.5px;font-weight:300;color:var(--white)}
.image-text .body{position:absolute;left:19px;top:77px;width:117px;color:#e6eef8;font-size:4.3px;line-height:6.2px;text-align:justify}
/* closing */
.closing .brand{position:absolute;left:36px;top:28px;display:flex;align-items:center;gap:5px;font-size:8px}
.closing .brand .mark{width:10px;height:10px;background:var(--sky)}
.thanks{position:absolute;left:25px;top:98px;color:var(--white)}
.thanks b{display:block;font-family:"Roboto Condensed",Arial Narrow,sans-serif;font-size:9.5px;letter-spacing:-.2px}
.thanks span{display:block;font-size:10px;font-weight:300}
.contact{position:absolute;left:26px;list-style:none}
.contact li{display:flex;align-items:center;gap:6px;height:17.5px;font-size:5px;color:#d7e8f7}
.contact .ico{width:8px;height:8px;border-radius:50%;background:var(--white)}
</style>
</head>
<body>

<!-- Cover -->
<section class="slide c1 r1 cover">
  <svg class="abs" style="left:0;top:0" width="355" height="200" viewBox="0 0 355 200">
    <path d="M0 155 L0 115 Q150 110 175 85 Q190 62 220 62 L355 62 L355 155 Z" fill="var(--green)"/>
    <rect x="0" y="195" width="355" height="5" fill="var(--blue)"/>
  </svg>
  <div class="photo" role="img" aria-label="Row of glass spheres with one orange sphere" style="left:0;top:78px;width:180px;height:77px;background:linear-gradient(90deg,#eef2f0 0%,#b9c7c1 30%,#d6e1d2 50%,#c36a32 68%,#b8c8a4 82%,#abd036 100%);opacity:.95"></div>
  <div class="brand"><span class="mark"></span><span class="brand-name">BIRCHPOINT CONSULTING</span></div>
  <div class="welcome">
    <h1>WELCOME</h1>
    <p class="sub">TO OUR PRESENTATION</p>
    <p class="date">Birmingham, March 25, 2011</p>
  </div>
  <p class="legal">© 2011 Birchpoint Consulting. All rights reserved. Contains confidential and proprietary information and may not be shared or reproduced without the prior written consent of the firm.</p>
  <div class="partner">Halvern Health</div>
</section>

<!-- Table of contents -->
<section class="slide c2 r1">
  <p class="toc-kicker">TABLE OF</p>
  <h2 class="toc-title">CONTENTS</h2>
  <ul class="toc-list" style="left:54px">
    <li><span class="dot">1</span>LOREM IPSUM DOLOR SIT MET</li>
    <li><span class="dot">1</span>LOREM IPSUM DOLOR SIT MET</li>
    <li><span class="dot">1</span>LOREM IPSUM DOLOR SIT MET</li>
  </ul>
  <ul class="toc-list" style="left:200px">
    <li><span class="dot">1</span>LOREM IPSUM DOLOR SIT MET</li>
    <li><span class="dot">1</span>LOREM IPSUM DOLOR SIT MET</li>
    <li><span class="dot">1</span>LOREM IPSUM DOLOR SIT MET</li>
  </ul>
</section>

<!-- Vision & mission -->
<section class="slide c3 r1 vision">
  <div class="photo" role="img" aria-label="Blue-tinted business meeting with charts on a desk" style="left:0;top:0;width:355px;height:110px;background:linear-gradient(120deg,#1b73be 0%,#3d8fcf 45%,#2a7cc4 70%,#1666b0 100%)"></div>
  <div class="abs" style="left:0;top:110px;width:355px;height:90px;background:var(--green)"></div>
  <p class="label">VISION &amp; MISSION</p>
  <div class="pillar" style="left:56px">
    <div class="badge">
      <svg width="20" height="12" viewBox="0 0 20 12"><circle cx="5" cy="7" r="4" fill="none" stroke="#fff" stroke-width="1.8"/><circle cx="15" cy="7" r="4" fill="none" stroke="#fff" stroke-width="1.8"/><rect x="8" y="4" width="4" height="3" fill="#fff"/></svg>
    </div>
    <p>To provide state of the art logistical and supply chain solutions to the defined needs of our customers using the best people, processes and systems in creating efficient and effective results.</p>
  </div>
  <div class="pillar" style="left:201px">
    <div class="badge">
      <svg width="20" height="16" viewBox="0 0 20 16"><path d="M2 14 A8 8 0 1 1 18 14" fill="none" stroke="#fff" stroke-width="1.8"/><line x1="10" y1="12" x2="14" y2="6" stroke="#fff" stroke-width="1.6"/><circle cx="10" cy="12" r="1.6" fill="#fff"/></svg>
    </div>
    <p>To provide state of the art logistical and supply chain solutions to the defined needs of our customers using the best people, processes and systems in creating efficient and effective results.</p>
  </div>
</section>

<!-- About us 1 -->
<section class="slide c1 r2">
  <h2 class="slide-title">ABOUT US</h2><div class="title-rule"></div>
  <div class="abs" style="left:0;top:49px;width:115px;height:65px;background:var(--green)"></div>
  <p class="abs" style="left:21px;top:71px;width:88px;font-size:3.8px;line-height:5.6px;color:#fff">LOREM IPSUM DOLOR SIT MET CONSECTETUR ADIPISCING ELIT, SED DO EIUSMOD TEMPOR INCIDIDUNT UT LABORE ET DOLORE MAGNA</p>
  <div class="photo" role="img" aria-label="Black and white photo of a smiling business team" style="left:115px;top:49px;width:240px;height:65px;background:linear-gradient(90deg,#5d5d5d,#bdbdbd 40%,#7a7a7a 65%,#d8d8d8)"></div>
  <p class="tiny abs" style="left:115px;top:124px;width:225px;font-size:4.4px;line-height:6.4px;color:var(--ink)">Lorem ipsum dolor sit amet, consectetur adipiscing elit, sed do eiusmod tempor incididunt ut labore et dolore magna aliqua. Ut enim ad minim veniam, quis nostrud exercitation ullamco laboris nisi ut aliquip ex ea commodo consequat. Duis aute irure dolor in reprehenderit in voluptate velit esse cillum dolore eu fugiat nulla pariatur.</p>
  <div class="footer-brand"><span class="mark"></span>BIRCHPOINT<span>Halvern Health</span></div>
  <svg class="footer-band" viewBox="0 0 355 8"><rect x="0" y="5.5" width="355" height="2.5" fill="var(--green)"/><path d="M275 8 L285 2 L355 2 L355 8 Z" fill="var(--blue)"/></svg>
  <span class="page-no">02</span>
</section>

<!-- About us 2 -->
<section class="slide c2 r2">
  <h2 class="slide-title">ABOUT US</h2><div class="title-rule"></div>
  <div class="photo" role="img" aria-label="Small photo of colleagues meeting at a table" style="left:33px;top:50px;width:70px;height:36px;background:linear-gradient(90deg,#e9e9e9,#8d8d8d 50%,#d0d0d0)"></div>
  <p class="abs" style="left:33px;top:92px;width:70px;text-align:center;font-size:4.3px;line-height:6px;color:var(--green-dark)">Lorem ipsum dolor sit amet consectetur adipiscing elitsed do eiusmod</p>
  <div class="abs tiny" style="left:108px;top:53px;width:110px;font-size:4px;line-height:6.1px;color:var(--ink)">
    <p>Lorem ipsum dolor sit amet, consectetur adipiscing elit, sed do eiusmod tempor incididunt ut labore et dolore magna aliqua. Ut enim ad minim veniam, quis nostrud exercitation ullamco laboris nisi ut aliquip ex ea commodo consequat. Duis aute irure dolor in reprehenderit in voluptate velit esse cillum dolore eu fugiat nulla pariatur.</p>
    <p style="margin-top:5px">Lorem ipsum dolor sit amet, consectetur adipiscing elit, sed do eiusmod tempor incididunt ut labore et dolore magna aliqua. Ut enim ad minim veniam, quis nostrud exercitation ullamco laboris nisi ut aliquip ex ea commodo</p>
  </div>
  <div class="abs tiny" style="left:232px;top:53px;width:110px;font-size:4px;line-height:6.1px;color:var(--ink)">
    <p>Lorem ipsum dolor sit amet, consectetur adipiscing elit, sed do eiusmod tempor incididunt ut labore et dolore magna aliqua. Ut enim ad minim veniam, quis nostrud exercitation ullamco laboris nisi ut aliquip ex ea commodo consequat. Duis aute irure dolor in reprehenderit in voluptate velit esse cillum dolore eu fugiat nulla pariatur.</p>
    <p style="margin-top:5px">Lorem ipsum dolor sit amet, consectetur adipiscing elit, sed do eiusmod tempor incididunt ut labore et dolore magna aliqua. Ut enim ad minim veniam, quis nostrud exercitation ullamco laboris nisi ut aliquip ex ea commodo</p>
  </div>
  <div class="footer-brand"><span class="mark"></span>BIRCHPOINT<span>Halvern Health</span></div>
  <svg class="footer-band" viewBox="0 0 355 8"><rect x="0" y="5.5" width="355" height="2.5" fill="var(--green)"/><path d="M275 8 L285 2 L355 2 L355 8 Z" fill="var(--blue)"/></svg>
  <span class="page-no">02</span>
</section>

<!-- Team -->
<section class="slide c3 r2">
  <h2 class="slide-title">OUR TEAM</h2><div class="title-rule"></div>
  <div class="member" style="left:33px">
    <div class="portrait" role="img" aria-label="Portrait of Jonathan Doe" style="background:radial-gradient(circle at 50% 40%,#b48a6e,#4b3a30)"></div>
    <h3>JONATHAN DOE</h3><h4>President</h4>
    <p class="tiny center">dolor sit amet, consectetur adipiscing elit, sed do eiusmod tempor incididunt ut labore et dolore magna aliqua. Ut enim ad minim veniam, quis nostrud exercitation ullamco laboris nisi ut aliquip ex ea commodo fugiat nulla pariatur.</p>
  </div>
  <div class="member" style="left:140px">
    <div class="portrait" role="img" aria-label="Portrait of Melanie Doe" style="background:radial-gradient(circle at 50% 40%,#b48a6e,#4b3a30)"></div>
    <h3>MELANIE DOE</h3><h4>CEO / Founder</h4>
    <p class="tiny center">dolor sit amet, consectetur adipiscing elit, sed do eiusmod tempor incididunt ut labore et dolore magna aliqua. Ut enim ad minim veniam, quis nostrud exercitation ullamco laboris nisi ut aliquip ex ea commodo fugiat nulla pariatur.</p>
  </div>
  <div class="member" style="left:253px">
    <div class="portrait" role="img" aria-label="Portrait of Natalie Doe" style="background:radial-gradient(circle at 50% 40%,#b48a6e,#4b3a30)"></div>
    <h3>NATALIE DOE</h3><h4>Vice President</h4>
    <p class="tiny center">dolor sit amet, consectetur adipiscing elit, sed do eiusmod tempor incididunt ut labore et dolore magna aliqua. Ut enim ad minim veniam, quis nostrud exercitation ullamco laboris nisi ut aliquip ex ea commodo fugiat nulla pariatur.</p>
  </div>
  <div class="footer-brand"><span class="mark"></span>BIRCHPOINT<span>Halvern Health</span></div>
  <svg class="footer-band" viewBox="0 0 355 8"><rect x="0" y="5.5" width="355" height="2.5" fill="var(--green)"/><path d="M275 8 L285 2 L355 2 L355 8 Z" fill="var(--blue)"/></svg>
  <span class="page-no">02</span>
</section>

<!-- Chart donuts -->
<section class="slide c1 r3">
  <h2 class="slide-title">OUR CHART</h2><div class="title-rule"></div>
  <div class="donut" style="left:24px">
    <svg width="48" height="48" viewBox="0 0 48 48"><g transform="rotate(-90 24 24)" fill="none" stroke-width="5"><circle cx="24" cy="24" r="20" stroke="var(--grey)"/><circle cx="24" cy="24" r="20" stroke="var(--mid-blue)" stroke-dasharray="101.8 125.7"/><circle cx="24" cy="24" r="20" stroke="var(--green)" stroke-dasharray="40 125.7"/></g><text x="24" y="27" text-anchor="middle" font-size="9" font-weight="600" fill="var(--mid-blue)" font-family="Open Sans,sans-serif">81%</text></svg>
    <p class="tiny center">dolor sit amet, consectetur adipiscing elit, sed do eiusmod tempor incididunt ut labore et dolore magna aliqua. Ut enim ad minim veniam, quis nostrud exercitation ullamco laboris nisi ut aliquip ex ea fugiat nulla pariatur</p>
  </div>
  <div class="donut" style="left:129px">
    <svg width="48" height="48" viewBox="0 0 48 48"><g transform="rotate(-90 24 24)" fill="none" stroke-width="5"><circle cx="24" cy="24" r="20" stroke="var(--grey)"/><circle cx="24" cy="24" r="20" stroke="var(--mid-blue)" stroke-dasharray="90.5 125.7"/><circle cx="24" cy="24" r="20" stroke="var(--green)" stroke-dasharray="45 125.7"/></g><text x="24" y="27" text-anchor="middle" font-size="9" font-weight="600" fill="var(--mid-blue)" font-family="Open Sans,sans-serif">72%</text></svg>
    <p class="tiny center">dolor sit amet, consectetur adipiscing elit, sed do eiusmod tempor incididunt ut labore et dolore magna aliqua. Ut enim ad minim veniam, quis nostrud exercitation ullamco laboris nisi ut aliquip ex ea fugiat nulla pariatur</p>
  </div>
  <div class="donut" style="left:230px">
    <svg width="48" height="48" viewBox="0 0 48 48"><g transform="rotate(-90 24 24)" fill="none" stroke-width="5"><circle cx="24" cy="24" r="20" stroke="var(--grey)"/><circle cx="24" cy="24" r="20" stroke="var(--mid-blue)" stroke-dasharray="79.2 125.7"/></g><text x="24" y="27" text-anchor="middle" font-size="9" font-weight="600" fill="var(--mid-blue)" font-family="Open Sans,sans-serif">63%</text></svg>
    <p class="tiny center">dolor sit amet, consectetur adipiscing elit, sed do eiusmod tempor incididunt ut labore et dolore magna aliqua. Ut enim ad minim veniam, quis nostrud exercitation ullamco laboris nisi ut aliquip ex ea fugiat nulla pariatur</p>
  </div>
  <div class="footer-brand"><span class="mark"></span>BIRCHPOINT<span>Halvern Health</span></div>
  <svg class="footer-band" viewBox="0 0 355 8"><rect x="0" y="5.5" width="355" height="2.5" fill="var(--green)"/><path d="M275 8 L285 2 L355 2 L355 8 Z" fill="var(--blue)"/></svg>
  <span class="page-no">02</span>
</section>

<!-- Chart bars -->
<section class="slide c2 r3">
  <h2 class="slide-title">OUR CHART</h2><div class="title-rule"></div>
  <div class="abs tiny" style="left:32px;top:60px;width:154px;font-size:3.9px;line-height:5.6px;color:var(--ink)">
    <p style="color:var(--sky)">Lorem ipsum dolor sit amet</p>
    <p>consectetur adipiscing elit, sed do eiusmod tempor incididunt ut labore et dolore magna aliqua. Ut enim ad minim veniam, quis nostrud exercitation ullamco laboris nisi ut aliquip ex ea commodo consequat. Duis aute irure dolor in reprehenderit in voluptate velit esse cillum dolore eu fugiat nulla pariatur</p>
    <p style="color:var(--sky);margin-top:4px">Lorem ipsum dolor sit amet</p>
    <p>consectetur adipiscing elit, sed do eiusmod tempor incididunt ut labore et dolore magna aliqua. Ut enim ad minim veniam, quis nostrud exercitation ullamco laboris nisi ut aliquip ex ea commodo consequat. Duis aute irure dolor in reprehenderit in voluptate velit esse cillum dolore eu</p>
    <p style="color:var(--sky);margin-top:4px">Lorem ipsum dolor sit amet</p>
    <p>Excepteur sint occaecat cupidatat non proident, sunt in culpa qui officia deserunt mollit anim id est laborum. Excepteur sint occaecat cupidatat non</p>
  </div>
  <svg class="abs" style="left:222px;top:40px" width="120" height="72" viewBox="0 0 120 72">
    <g stroke="#d4d5d7" stroke-width=".4">
      <line x1="8" y1="2" x2="8" y2="61"/><line x1="6" y1="12" x2="10" y2="12"/><line x1="6" y1="24" x2="10" y2="24"/><line x1="6" y1="36" x2="10" y2="36"/><line x1="6" y1="48" x2="10" y2="48"/>
      <line x1="8" y1="61" x2="118" y2="61"/>
    </g>
    <rect x="14" y="34" width="6" height="27" fill="var(--mid-blue)"/><rect x="20" y="46" width="6" height="15" fill="var(--grey)"/><rect x="26" y="48" width="6" height="13" fill="var(--green)"/>
    <rect x="42" y="28" width="6" height="33" fill="var(--mid-blue)"/><rect x="48" y="22" width="6" height="39" fill="var(--grey)"/><rect x="54" y="44" width="6" height="17" fill="var(--green)"/>
    <rect x="70" y="27" width="6" height="34" fill="var(--mid-blue)"/><rect x="76" y="44" width="6" height="17" fill="var(--grey)"/><rect x="82" y="40" width="6" height="21" fill="var(--green)"/>
    <rect x="98" y="31" width="6" height="30" fill="var(--mid-blue)"/><rect x="104" y="47" width="6" height="14" fill="var(--grey)"/><rect x="110" y="22" width="6" height="39" fill="var(--green)"/>
    <rect x="47" y="15" width="8" height="4" fill="var(--grey)"/><rect x="75" y="20" width="8" height="4" fill="var(--mid-blue)"/><rect x="109" y="15" width="8" height="4" fill="var(--green)"/>
    <g font-size="3.6" fill="var(--ink)" font-family="Open Sans,sans-serif" text-anchor="middle"><text x="23" y="68">2009</text><text x="51" y="68">2010</text><text x="79" y="68">2011</text><text x="107" y="68">2012</text></g>
  </svg>
  <div class="legend">
    <p class="key"><span class="swatch" style="background:var(--mid-blue)"></span>LOREM IPSUM</p>
    <p>Lorem ipsum dolor sit amet consectetur adipiscing elit, sed do eiusmod tempor incididunt ut labore magna</p>
    <p class="key" style="margin-top:5px"><span class="swatch" style="background:var(--grey)"></span>LOREM IPSUM</p>
    <p>Lorem ipsum dolor sit amet consectetur adipiscing elit, sed do eiusmod tempor incididunt ut labore magna</p>
    <p class="key" style="margin-top:5px"><span class="swatch" style="background:var(--green)"></span>LOREM IPSUM</p>
  </div>
  <div class="footer-brand"><span class="mark"></span>BIRCHPOINT<span>Halvern Health</span></div>
  <svg class="footer-band" viewBox="0 0 355 8"><rect x="0" y="5.5" width="355" height="2.5" fill="var(--green)"/><path d="M275 8 L285 2 L355 2 L355 8 Z" fill="var(--blue)"/></svg>
  <span class="page-no">02</span>
</section>

<!-- Services -->
<section class="slide c3 r3">
  <h2 class="slide-title">OUR SERVICES</h2><div class="title-rule"></div>
  <div class="service" style="left:28px"><div class="head dark">
    <svg width="14" height="14" viewBox="0 0 14 14"><path d="M7 1 L13 7 L7 13 L1 7 Z" fill="#fff"/></svg>
    <span style="margin-top:4px">MANAGEMENT<br>SOLUTIONS</span></div>
    <p class="tiny">Dolor sit amet, consectetur adipiscing elit, sed do eiusmod tempor incididunt ut labore et dolore magna aliqua.</p></div>
  <div class="service" style="left:106px"><div class="head lime">
    <svg width="14" height="14" viewBox="0 0 14 14"><circle cx="7" cy="7" r="6" fill="none" stroke="#fff" stroke-width="1.2"/><text x="7" y="10.5" text-anchor="middle" font-size="9" font-style="italic" fill="#fff" font-family="Georgia,serif">i</text></svg>
    <span style="margin-top:4px">INFORMATION<br>SOLUTIONS</span></div>
    <p class="tiny">Dolor sit amet, consectetur adipiscing elit, sed do eiusmod tempor incididunt ut labore et dolore magna aliqua.</p></div>
  <div class="service" style="left:184px"><div class="head dark">
    <svg width="16" height="12" viewBox="0 0 16 12"><path d="M1 5 L5 2 L8 4 L11 2 L15 5 L10 10 L6 10 Z" fill="#fff"/></svg>
    <span style="margin-top:4px">PROFESSIONAL<br>SERVICES</span></div>
    <p class="tiny">Dolor sit amet, consectetur adipiscing elit, sed do eiusmod tempor incididunt ut labore et dolore magna aliqua.</p></div>
  <div class="service" style="left:262px"><div class="head lime">
    <svg width="14" height="14" viewBox="0 0 14 14"><g stroke="#fff" stroke-width="1"><line x1="7" y1="7" x2="7" y2="2"/><line x1="7" y1="7" x2="12" y2="9"/><line x1="7" y1="7" x2="2" y2="9"/></g><circle cx="7" cy="7" r="2" fill="#fff"/><circle cx="7" cy="2" r="1.5" fill="#fff"/><circle cx="12" cy="9" r="1.5" fill="#fff"/><circle cx="2" cy="9" r="1.5" fill="#fff"/></svg>
    <span style="margin-top:4px">ORGANIZATIONAL<br>TRANSFORMATION</span></div>
    <p class="tiny">Dolor sit amet, consectetur adipiscing elit, sed do eiusmod tempor incididunt ut labore et dolore magna aliqua.</p></div>
  <div class="footer-brand"><span class="mark"></span>BIRCHPOINT<span>Halvern Health</span></div>
  <svg class="footer-band" viewBox="0 0 355 8"><rect x="0" y="5.5" width="355" height="2.5" fill="var(--green)"/><path d="M275 8 L285 2 L355 2 L355 8 Z" fill="var(--blue)"/></svg>
  <span class="page-no">02</span>
</section>

<!-- Section divider -->
<section class="slide c1 r4">
  <svg class="abs" style="left:155px;top:78px" width="44" height="44" viewBox="0 0 44 44"><circle cx="22" cy="22" r="21" fill="var(--mid-blue)"/><circle cx="24" cy="11" r="3" fill="#fff"/><path d="M19 18 L27 18 L23 33 L26 33 L25 35 L16 35 L17 33 L19 33 L22 20 L18 20 Z" fill="#fff"/></svg>
  <div class="abs" style="left:133px;top:128px;width:90px;height:.7px;background:var(--ink)"></div>
  <p class="section-name">SECTION TITLE</p>
</section>

<!-- Image with text -->
<section class="slide c2 r4 image-text">
  <div class="panel"></div>
  <div class="photo" role="img" aria-label="Black and white photo of smiling business professionals" style="left:153px;top:0;width:202px;height:200px;background:linear-gradient(100deg,#3a3a3a 0%,#cfcfcf 35%,#f2f2f2 55%,#6d6d6d 80%,#a9a9a9 100%)"></div>
  <h2>IMAGE TEXT</h2>
  <p class="body">Lorem ipsum dolor sit amet, consectetur adipiscing elit, sed do eiusmod tempor incididunt ut labore et dolore magna aliqua. Ut enim ad minim veniam, quis nostrud exercitation ullamco laboris nisi ut aliquip ex ea commodo consequat. Duis aute irure dolor in reprehenderit in voluptate velit esse cillum dolore eu fugiat nulla pariatur.</p>
  <div class="abs" style="left:7px;bottom:6px;display:flex;align-items:center;gap:3px;font-size:4px;font-weight:700;color:#fff"><span style="width:5px;height:5px;background:#fff"></span>BIRCHPOINT</div>
</section>

<!-- Closing -->
<section class="slide c3 r4 closing">
  <svg class="abs" style="left:0;top:0" width="355" height="200" viewBox="0 0 355 200">
    <defs><linearGradient id="closingBlue" x1="0" y1="0" x2="1" y2="1"><stop offset="0" stop-color="#0a5aa8"/><stop offset=".6" stop-color="#1f7fc4"/><stop offset="1" stop-color="#0355a3"/></linearGradient></defs>
    <path d="M0 200 L0 80 L160 80 Q180 80 192 70 Q205 60 225 60 L355 60 L355 200 Z" fill="url(#closingBlue)"/>
    <rect x="0" y="195" width="355" height="5" fill="var(--green)"/>
  </svg>
  <div class="brand"><span class="mark"></span><span class="brand-name">BIRCHPOINT CONSULTING</span></div>
  <div class="thanks"><b>THANK YOU</b><span>FOR YOUR TIME</span></div>
  <ul class="contact" style="top:138px">
    <li><span class="ico"></span>412 Alder Court Ste 300</li>
    <li><span class="ico"></span>hello@birchpoint.example</li>
    <li><span class="ico"></span>www.birchpoint.example</li>
  </ul>
</section>

</body>
</html>
```